Psychology practice Logo and Business card design

Still in its early development, Meridian Counselling Group provides comprehensive psychology services to a diverse range of clients in the Barossa Valley. Some details available on website - www.tallowmind-example.com.
The Barossa is a semi-rural area, famous for our wines.
At Meridian Counselling Group we work with young children, adolescents, families and adults. We will soon move into our own premises in a restored historic/heritage building in the main street of Angaston. This 1870s building was most recently a bookshop, but has previously been a grocer store and secret 'clubhouse'.
The preferred therapeutic style of our psychologist is called RFT therapy - this is in part how the name of the business was decided. We are also encouraging of clients' physical health in conjunction with their emotional health.
Updates

Thank you to those designers who have already provided early ideas.

A few extra thoughts:

- given the national psychology body is the NBT, I'm keen to avoid using that abbreviation;

- simple is best;

- I would prefer the business name to be the feature rather than my own name;

- a simple logo as part of the design would be fantastic so it can be adapted for signage etc.

Many thanks for your continued help.

Target Market(s)

broad - adults, adolescents, families.

Industry/Entity Type

Building

Contact Information for Business Card

Meridian Counselling Group
www. tallowmind-example.com

PO Box 714
Kelverton SA 5377

Delia Farrant FNBT
Psychologist
BSc, Grad Dip Ed, M Psych (Clinical)
mob: 0431 957 284
fax: 0869 413 508
email: delia@tallowmind-example.com

Requirements
Must have
• Simple logo design included.
All contact information.
Reverse side for appointment details (Next appointment: Date, Time)
Nice to have
• Something representative of hope / future focus.
Possibly a combination of modern feel with connection to heritage?
Gender neutral colours
Should not have
• abbreviation to NBT
photograph

```html
<!DOCTYPE html>
<html lang="en">
<head>
<meta charset="utf-8">
<title>Meridian Counselling Group – Business Card</title>
<link rel="stylesheet" href="https://fonts.googleapis.com/css2?family=Belleza&display=swap">
<style>
  :root {
    --backdrop: #262626;
    --card-light: #dcdcdc;
    --card-dark: #4a4a4a;
    --accent: #f39a1e;
    --ink-grey: #4d4d4d;
    --ink-white: #f2f2f2;
  }
  * { box-sizing: border-box; margin: 0; padding: 0; }
  html, body {
    width: 1200px; height: 900px; overflow: hidden;
    background: var(--backdrop);
    font-family: "Belleza", "Optima", sans-serif;
  }
  .canvas {
    position: relative; width: 1200px; height: 900px;
    display: flex; align-items: center; justify-content: center; gap: 60px;
  }
  .card {
    position: relative; width: 520px; height: 318px;
    border-bottom: 5px solid var(--accent);
  }
  .card--front {
    background: var(--card-light);
    display: flex; align-items: center; justify-content: center; gap: 16px;
  }
  .brand-square {
    width: 22px; height: 22px;
    background: var(--accent);
    flex: none;
  }
  .brand-name {
    color: var(--ink-grey); font-size: 34px; font-weight: 400; letter-spacing: 0.5px;
    white-space: nowrap;
  }
  .card--back {
    background: var(--card-dark);
    display: flex; flex-direction: column; align-items: center; justify-content: center;
    text-align: center; color: var(--ink-white);
  }
  .holder-name { color: var(--accent); font-size: 28px; font-weight: 400; margin-bottom: 2px; }
  .credentials { font-size: 13px; margin-bottom: 8px; }
  .practice { color: var(--accent); font-size: 17px; }
  .address { font-size: 14px; margin-bottom: 4px; }
  .contact-line { font-size: 13.5px; white-space: nowrap; }
  .label { color: var(--accent); }
  .website { font-size: 18px; margin-top: 8px; }
  .website .domain { color: var(--accent); }
</style>
</head>
<body>
<main class="canvas">
  <section class="card card--front" aria-label="Card front">
    <span class="brand-square" aria-hidden="true"></span>
    <h1 class="brand-name">Meridian Counselling Group</h1>
  </section>

  <section class="card card--back" aria-label="Card back">
    <h2 class="holder-name">Delia Farrant</h2>
    <p class="credentials">FNBT Psychologist BSc, Grad Dip Ed, M Psych (Clinical)</p>
    <p class="practice">Meridian Counselling Group</p>
    <p class="address">PO Box 714 Kelverton SA 5377</p>
    <p class="contact-line">
      <span class="label">mob:</span> 0431 957 284&nbsp;&nbsp;
      <span class="label">fax:</span> 0869 413 508&nbsp;&nbsp;
      <span class="label">email:</span> delia@tallowmind-example.com
    </p>
    <p class="website">www.<span class="domain">tallowmind-example</span>.com</p>
  </section>
</main>
</body>
</html>
```